RK Bastone Construction Inc.

Design a new business card for our construction company
To be removed from current card:
Delete 25 years
Delete Tenant fit up Renovations section

```html
<!DOCTYPE html>
<html lang="en">
<head>
<meta charset="utf-8">
<title>RK Bastone Construction Inc. – Business Card</title>
<link rel="stylesheet" href="https://fonts.googleapis.com/css2?family=Saira:wght@400;600;700&display=swap">
<style>
  :root {
    --backdrop: #979797;
    --card: #ffffff;
    --brand-purple: #552d73;
    --ink: #4f2c6e;
  }
  * { box-sizing: border-box; margin: 0; padding: 0; }
  html, body {
    width: 1200px; height: 1000px; overflow: hidden;
    background: var(--backdrop);
    font-family: "Saira", Arial, sans-serif;
  }
  .card {
    position: absolute;
    width: 615px; height: 351px;
    background: var(--card);
    box-shadow: 0 14px 40px rgba(0,0,0,0.45);
    color: var(--ink);
    text-align: center;
  }
  .card--front { left: 293px; top: 100px; }
  .card--back  { left: 295px; top: 511px; }

  .wordmark {
    position: absolute; left: 0; right: 0;
    color: var(--brand-purple);
    font-weight: 600;
    font-size: 25px;
    line-height: 27px;
    letter-spacing: 1.5px;
    text-transform: uppercase;
  }
  .card--front .wordmark { top: 148px; }
  .card--back .wordmark { top: 38px; }

  .holder-name {
    position: absolute; left: 0; right: 0; top: 144px;
    font-size: 23px; font-weight: 700; line-height: 30px;
  }
  .holder-mobile {
    position: absolute; left: 0; right: 0; top: 176px;
    font-size: 22px; font-weight: 700; letter-spacing: 1.5px; line-height: 30px;
  }
  .contact {
    position: absolute; left: 0; right: 0;
    font-size: 19px; line-height: 24px; white-space: nowrap;
  }
  .contact--address { top: 254px; padding-left: 44px; }
  .contact--lines { top: 278px; font-size: 18.5px; padding-left: 16px; }
  .contact--web { top: 302px; font-size: 18.5px; }
  .contact .email { font-weight: 700; margin-left: 10px; }
  .icon { display: inline-block; vertical-align: -1px; fill: var(--ink); }
</style>
</head>
<body>
  <section class="card card--front" aria-label="Card front">
    <div class="wordmark">RK Bastone<br>Construction Inc.</div>
  </section>

  <section class="card card--back" aria-label="Card back">
    <div class="wordmark">RK Bastone<br>Construction Inc.</div>

    <p class="holder-name">Marco Bastone</p>
    <p class="holder-mobile">
      <svg class="icon" width="11" height="17" viewBox="0 0 11 17"><path d="M2 0h7a2 2 0 0 1 2 2v13a2 2 0 0 1-2 2H2a2 2 0 0 1-2-2V2a2 2 0 0 1 2-2zm0 2v11h7V2zm3.5 12a1 1 0 1 0 0 2 1 1 0 0 0 0-2z"/></svg>
      613-555-0147
    </p>

    <p class="contact contact--address">2180 Meadowlark Rd., Suite 100, Ottawa, ON K1B 4R7</p>
    <p class="contact contact--lines">
      <svg class="icon" width="18" height="13" viewBox="0 0 18 13"><path d="M1 4C3 0 15 0 17 4l-3 1-1-2H5L4 5zM4 6h10l2 7H2zm5 1.5a2.5 2.5 0 1 0 0 5 2.5 2.5 0 0 0 0-5z"/></svg>
      613-555-0182 ext. 221
      <span class="email"><svg class="icon" width="16" height="11" viewBox="0 0 16 11"><path d="M0 0h16v11H0zm1.5 1.5v8h13v-8L8 6.5z"/></svg>
      marco@rkbastoneconst.ca</span>
    </p>
    <p class="contact contact--web">
      <svg class="icon" width="13" height="13" viewBox="0 0 13 13"><circle cx="6.5" cy="6.5" r="5.7" fill="none" stroke="#4f2c6e" stroke-width="1.3"/><path d="M1 6.5h11M6.5 1v11" stroke="#4f2c6e" stroke-width="1.1" fill="none"/><ellipse cx="6.5" cy="6.5" rx="2.6" ry="5.7" fill="none" stroke="#4f2c6e" stroke-width="1.1"/></svg>
      www.rkbastoneconst.ca
    </p>
  </section>
</body>
</html>
```